Broschüre für Immobilienvertrieb
Zielgruppe
Wir sind ein Immobilienvertrieb im Bereich Neubau-Immobilien und Bestand-Immobilien aus München. Die Firma BLOR existiert seit über 30 Jahren. Vor 4 Jahren haben wir ein cooles modernes Rebranding durchgeführt, sodass man mit unserem neuen Corporate Design richtig Spaß am Gestalten haben kann.
Eine konkrete Zielgruppe zu definieren ist schwierig, da unsere Käufer von 20-80 Jahren sein können. Ob junge, erfolgreiche Menschen, junge Familien, ältere Erwachsene, die von sich nach Auszug ihrer Kinder von ihrem Haus trennen wollen und eine kleinere Wohnung suchen oder einfach der Kapitalanleger, der auf der Suche nach einer neuen Investition ist.
Unsere CI ist gradlinig und setzt sich aus anthrazit, neonorange und weiß zusammen (Styleguide ist anbei).
Im Bestand gibt es nicht pro Objekt ein CI, hier wird mit dem der BLOR gearbeitet. Im Neubau hat jedes einzelne Projekt sein eigenes CI (siehe aktuell hausfeld-neu.de).
www.blor.de
Aufgabenstellung
Zur Aufgabe: Für die Bestandimmobilien benötigen wir ein neues Layout eines Immobilienexposé. Das Exposé wird sowohl online verwendet als auch von uns selbst gedruckt und gebunden.
Input: beigefügt ein Beispielexposé - grundsätzlich gefällt uns das Design, wir möchten jedoch etwas NEUES, modernes. Bitte keine Kopien des alten Exposés, dies soll nur als Input dienen (gerne können die Daten der Wohnung für den neuen Designentwurf genutzt werden).
Die Datei soll von uns befüllbar sein, sodass wir Texte und Bilder selbst austauschen können.
Für die Onlinenutzung gerne als doppelseitige Datei, zum Beispiel um Bilder über zwei Seiten größer und schöner darstellen zu können (Auszug Beispielimmobilie anbei). Für den Druck wird die Datei zudem mit Einzelseiten benötigt.

```html
<!DOCTYPE html>
<html lang="de">
<head>
<meta charset="utf-8">
<title>BLOR Exposé – Lindenallee München</title>
<link rel="stylesheet" href="https://fonts.googleapis.com/css2?family=Montserrat:wght@300;400;500;600;700;800&family=Nunito+Sans:wght@600;700;800&display=swap">
<style>
  :root{
    --orange:#e8512f;
    --orange-soft:#ee7b56;
    --orange-pale:#f3a887;
    --anthracite:#333539;
    --ink:#1e1f22;
    --white:#ffffff;
    --row-dark:#dfe4e8;
    --row-light:#f3f5f7;
    --stage:#e9e7e4;
  }
  *{box-sizing:border-box;margin:0;padding:0}
  html,body{width:1200px;height:900px;overflow:hidden;background:var(--stage)}
  body{font-family:"Montserrat",sans-serif;color:var(--ink);position:relative}

  .page{position:absolute;top:180px;width:382px;height:540px;background:var(--white);overflow:hidden;box-shadow:0 2px 10px rgba(0,0,0,.12)}

  /* Cover */
  .cover{left:14px;background:var(--anthracite)}
  .cover-photo{position:absolute;left:0;top:0;width:100%;height:382px;
    background:linear-gradient(160deg,#e4603a 0%,#ef8a55 45%,#e96a3e 75%,#d9572f 100%)}
  .cover-band{position:absolute;left:0;top:382px;width:100%;height:158px;background:var(--anthracite)}
  .frame-line{position:absolute;background:var(--white)}
  .frame-top{left:19px;top:19px;width:255px;height:2px}
  .frame-left{left:19px;top:19px;width:2px;height:488px}
  .frame-right{left:359px;top:19px;width:2px;height:494px}
  .frame-bottom{left:133px;top:511px;width:228px;height:2px}
  .brand{position:absolute;left:0;width:100%;top:66px;text-align:center;color:var(--white);
    font-weight:600;font-size:30px;letter-spacing:8px;padding-left:8px}
  .tagline{position:absolute;left:0;width:100%;top:126px;text-align:center;color:var(--white);
    font-weight:600;font-size:8.5px;letter-spacing:2px}
  .cover-title{position:absolute;left:0;width:100%;top:414px;text-align:center;color:var(--white);
    font-weight:600;font-size:16.5px;letter-spacing:3.4px;line-height:19px}
  .cover-sub{position:absolute;left:0;width:100%;top:460px;text-align:center;color:#ececec;
    font-weight:400;font-size:8.3px;letter-spacing:1.3px;line-height:11px}
  .cover-object{position:absolute;left:19px;top:506px;color:var(--white);font-weight:600;font-size:7.5px;letter-spacing:1.5px}

  /* Spread */
  .page-left{left:420px;background:#fcfcfd}
  .page-right{left:802px;border-left:1px solid #e3e3e3}
  .page-num{position:absolute;top:22px;font-size:5.5px;font-weight:700}
  .page-left .page-num{left:22px}
  .page-right .page-num{right:22px}
  .page-mark{position:absolute;top:24px;width:12px;height:4px;background:var(--orange)}
  .page-left .page-mark{left:4px}
  .page-right .page-mark{right:0}
  .headline{position:absolute;top:64px;left:21px;font-size:14.5px;letter-spacing:2px;font-weight:400;color:var(--ink)}
  .headline .plus{color:var(--orange);font-weight:700;font-size:11px;margin-right:4px}
  .headline strong{color:var(--orange);font-weight:700}
  .page-right .headline{left:17px}

  .feature-list{position:absolute;left:21px;top:142px;width:326px;list-style:none}
  .feature-list li{font-family:"Nunito Sans",sans-serif;font-weight:700;font-size:7.6px;letter-spacing:.5px;
    line-height:11.5px;text-transform:uppercase;margin-bottom:10.5px;color:var(--ink)}
  .feature-list li::before{content:"+ ";color:var(--orange);font-weight:800}

  .footer{position:absolute;left:0;width:100%;top:512px;text-align:center;font-size:5px;color:#333}
  .footer b{font-weight:700}

  .data-table{position:absolute;left:17px;top:101px;width:336px;border-collapse:collapse;
    font-family:"Nunito Sans",sans-serif;font-size:6.8px;text-align:center}
  .data-table td{height:12.7px;padding:0;color:var(--ink)}
  .data-table td:first-child{font-weight:800;letter-spacing:.5px;width:50%;border-right:1px solid #c9ced3}
  .data-table td:last-child{font-weight:700}
  .data-table tr:nth-child(odd){background:var(--row-dark)}
  .data-table tr:nth-child(even){background:var(--row-light)}

  .price-table{position:absolute;left:17px;top:447px;width:336px;border-collapse:collapse;
    font-family:"Nunito Sans",sans-serif;text-align:center;color:var(--white)}
  .price-table td{padding:0;font-weight:800}
  .price-table td:first-child{width:50%;border-right:1px solid rgba(255,255,255,.6);letter-spacing:.6px}
  .price-main{background:var(--orange-soft);height:14px;font-size:8.5px}
  .price-main td{letter-spacing:.8px}
  .price-pale{background:var(--orange-pale);height:13px;font-size:6.6px}
  .price-pale td{color:var(--anthracite)}
  .price-soft{background:var(--orange-soft);height:13px;font-size:6.6px}
</style>
</head>
<body>

<section class="page cover" aria-label="Titelseite">
  <div class="cover-photo" role="img" aria-label="Foto der Hausfassade mit Balkonen, orange eingefärbt"></div>
  <div class="cover-band"></div>
  <div class="frame-line frame-top"></div>
  <div class="frame-line frame-left"></div>
  <div class="frame-line frame-right"></div>
  <div class="frame-line frame-bottom"></div>
  <div class="brand">BLOR</div>
  <div class="tagline">WOHNRAUM MIT LEIDENSCHAFT</div>
  <h1 class="cover-title">LINDENALLEE<br>MÜNCHEN</h1>
  <p class="cover-sub">MÖBILIERTE &amp; GUT VERMIETETE KAPITALANLAGE<br>IN GUTER LAGE MIT BALKON &amp; STELLPLATZ</p>
  <div class="cover-object">OBJEKT XX - 2.OG</div>
</section>

<section class="page page-left" aria-label="Seite 6">
  <span class="page-mark"></span><span class="page-num">6</span>
  <h2 class="headline"><span class="plus">+</span>OBJEKT<strong>INFORMATIONEN</strong></h2>
  <ul class="feature-list">
    <li>Anschluss an das Fernwärmenetz 2016</li>
    <li>Sukzessiver Fenstertausch der Fenster in den<br>Wohnungen und Fluren/Treppenhaus</li>
    <li>Flursanierung in allen Stockwerken bereits durchgeführt</li>
    <li>Haustechnik: Einbau von Strangventilen, Entfernen von Totleitungen, Einbau einer intelligenten Steuerung der Warmwasserheizung</li>
    <li>Inbetriebnahme der intelligenten Aussentemperatur<br>Steuerung der Heizung zur Betriebskostensenkung</li>
    <li>Sanierung der Gemeinschaftsflächen bereits abgeschlossen</li>
    <li>Waschmaschinenraum im UG mit intelligentem<br>Waschmaschinenbuchungssystem</li>
    <li>Erneuerung der Aufzugstechnik bereits abgeschlossen</li>
    <li>Verlegung von Glasfaser direkt in alle Wohnungen</li>
    <li>Kickbox- und Fitnessstudio mit Mieteinnahme</li>
  </ul>
  <p class="footer"><b>Exposé</b> | Lindenallee 48 | Objektnr. XX - München</p>
</section>

<section class="page page-right" aria-label="Seite 7">
  <span class="page-mark"></span><span class="page-num">7</span>
  <h2 class="headline"><span class="plus">+</span>OBJEKT<strong>DATEN</strong></h2>
  <table class="data-table">
    <tr><td>OBJEKT-NR.</td><td>XX</td></tr>
    <tr><td>OBJEKTART</td><td>Wohnung</td></tr>
    <tr><td>OBJEKTTYP</td><td>Etagenwohnung</td></tr>
    <tr><td>STRASSE</td><td>Lindenallee</td></tr>
    <tr><td>HAUSNUMMER</td><td>48</td></tr>
    <tr><td>PLZ</td><td>80799</td></tr>
    <tr><td>STADT</td><td>München</td></tr>
    <tr><td>ETAGE</td><td>2. OG</td></tr>
    <tr><td>ETAGENANZAHL</td><td>15</td></tr>
    <tr><td>WOHNFLÄCHE</td><td>ca. 32,39 m²</td></tr>
    <tr><td>ANZAHL ZIMMER</td><td>1</td></tr>
    <tr><td>ANZAHL BADEZIMMER</td><td>1</td></tr>
    <tr><td>ZUSTAND</td><td>gepflegt</td></tr>
    <tr><td>BAUJAHR</td><td>1972</td></tr>
    <tr><td>WESENTLICHER ENERGIETRÄGER</td><td>Fernwärme</td></tr>
    <tr><td>HEIZUNGSART</td><td>Zentralheizung</td></tr>
    <tr><td>ENERGIEAUSWEIS</td><td>Bedarfsausweis</td></tr>
    <tr><td>ENERGIEVERBRAUCH</td><td>107,15 kWh/(m2*a)</td></tr>
    <tr><td>ENERGIEAUSWEIS GÜLTIG BIS</td><td>19.08.2028</td></tr>
    <tr><td>BAUJAHR LT. ENERGIEAUSWEIS</td><td>1973</td></tr>
    <tr><td>FAHRSTUHL</td><td>Personenaufzug</td></tr>
    <tr><td>KABEL SAT TV</td><td>Ja</td></tr>
    <tr><td>BALKON</td><td>Ja</td></tr>
    <tr><td>VERMIETET</td><td>Ja</td></tr>
    <tr><td>VERFÜGBAR AB</td><td>nach Vereinbarung</td></tr>
    <tr><td>HAUSGELD</td><td>214,00 €</td></tr>
  </table>
  <table class="price-table">
    <tr class="price-main"><td>KAUFPREIS</td><td>XXX.XXX €</td></tr>
    <tr class="price-pale"><td>AUSSENPROVISION</td><td>x,xx % inkl. USt. des Kaufpreises</td></tr>
    <tr class="price-soft"><td>STELLPLATZ</td><td>1 Freiplatz à xx.000,00 € (Kauf)</td></tr>
  </table>
  <p class="footer"><b>Exposé</b> | Lindenallee 48 | Objektnr. XX - München</p>
</section>

</body>
</html>
```